Bring me business with this creative business card

Design my new business card. I am looking for something different with an impact. People will take a look at this card & they will 1- see how different & creative I am, 2-understand what I do 3- Call me to meet me!

I make videos with a message, testimonials. I am dynamic, fun, creative & human. My new website is in construction but in the meantime you can check this old one: brightpath.ca & another one Fernquill.com & fernquill facebook page.
I make videos. sometimes with a cameraman, sometimes with my phone. As an ex Public Relations agent, the message is the most important thing for me. I want to make my clients shine! When they start with me they often remind me of a lamb, when I finish coaching them they are powerful like LIONS! That's why I need a powerful business card!

Target Market(s)

Entrepreneurs, solo entrepreneurs, small & medium companies & start ups. People i will meet while networking. People that need videos on their website & social Networks to get attention, to be visible. men & women. From 35 to 49 years old.
I am an ex Public relations agent. I used to send clients in traditional medias, now with videos they have more chances to be seen on google the new media. I do videos of the president, his team, his loyal clients saying how great the company is & expert videos like series so people can be seen for example every 1 st of every month with a short 2 minute video. Also with my 20 years in marketing & communications I can coach & give tips to anybody who needs it.
Target: anybody who would like my old website brightpath.ca & I also have another website but it will be off line soon: fernquill.com could give you ideas.

Industry/Entity Type

Communications

Contact Information for Business Card

I am in Montreal,So the business cards have to be the usual size like we have in Montreal: 9 cm x 5 cm
Details:My text: Corinne Vautrin Communication coach/Lead Storyteller. "Telling Stories as bold as you" off: 514-555-0147 cell: 514-555-0183. fernquill.com
corinne@fernquill.com logo facebook, youtube, instagram

Colors
f37122

Requirements
Must have
• Dynamic, happy. Orange. Be creative in the look but NOT the shape of the card. Easy to read. Big enough to read.
Should not have
• No funny shapes: no round, no square, just the usual. I love creative but NOT on shape.

```html
<!DOCTYPE html>
<html lang="en">
<head>
<meta charset="utf-8">
<title>Fernquill Business Card</title>
<link rel="stylesheet" href="https://fonts.googleapis.com/css2?family=Roboto+Condensed:wght@700&family=Roboto:wght@400;500&display=swap">
<style>
  :root {
    --page-bg: #e6e1db;
    --orange: #f37122;
    --orange-deep: #ec6a12;
    --orange-dark: #e2581a;
    --amber: #f9a21c;
    --yellow: #f8d21c;
    --white: #ffffff;
    --paper: #f6f6f5;
    --ink-orange: #e7661f;
    --gold: #e9a532;
  }
  * { margin: 0; padding: 0; box-sizing: border-box; }
  html, body { width: 1200px; height: 960px; overflow: hidden; }
  body { background: var(--page-bg); position: relative; font-family: "Roboto", Arial, sans-serif; }

  .card { position: absolute; width: 600px; height: 343px; box-shadow: 0 3px 8px rgba(0,0,0,.25); overflow: hidden; }

  /* Front */
  .card-front { left: 314px; top: 113px; background: var(--orange); }
  .pattern-top, .pattern-bottom { position: absolute; left: 0; width: 100%; }
  .pattern-top { top: 0; height: 109px; background: linear-gradient(100deg, var(--yellow) 0%, var(--amber) 30%, var(--orange) 55%, var(--amber) 78%, var(--yellow) 100%); }
  .pattern-bottom { top: 235px; height: 108px; background: linear-gradient(80deg, var(--orange-dark) 0%, var(--amber) 30%, var(--orange) 55%, var(--amber) 78%, var(--orange-dark) 100%); }
  .info-band { position: absolute; left: 0; top: 109px; width: 100%; height: 126px; background: var(--orange-deep); }
  .identity { position: absolute; right: 329px; top: 133px; text-align: right; color: var(--white); }
  .identity .name { font-family: "Roboto Condensed", "Arial Narrow", sans-serif; font-weight: 700; font-size: 32px; line-height: 38px; letter-spacing: .3px; }
  .identity .role { font-size: 15px; line-height: 19px; text-transform: uppercase; margin-top: 2px; }
  .divider { position: absolute; left: 299px; top: 126px; width: 2px; height: 92px; background: rgba(255,255,255,.85); }
  .contacts { position: absolute; left: 326px; top: 134px; list-style: none; color: var(--white); font-size: 14.5px; line-height: 19.3px; }
  .contacts li { display: flex; align-items: center; gap: 8px; }
  .contacts svg { width: 13px; height: 13px; fill: var(--white); flex: none; }

  /* Back */
  .card-back { left: 311px; top: 472px; background: var(--paper); text-align: center; }
  .brand-mark { position: absolute; left: 250px; top: 62px; width: 100px; height: 100px; border-radius: 50%; background: var(--orange); }
  .brand-name { position: absolute; left: 0; width: 100%; top: 196px; font-family: "Roboto Condensed", "Arial Narrow", sans-serif; font-weight: 700; font-size: 34px; line-height: 40px; letter-spacing: 2px; color: var(--ink-orange); }
  .motto { position: absolute; left: 0; width: 100%; top: 236px; display: flex; justify-content: center; align-items: center; gap: 6px; font-size: 13px; color: var(--gold); letter-spacing: .5px; }
  .motto::before, .motto::after { content: ""; width: 30px; height: 1px; background: var(--gold); }
  .tagline { position: absolute; left: 0; width: 100%; top: 255px; font-size: 14px; font-weight: 500; color: var(--ink-orange); }
  .social-row { position: absolute; left: 170px; width: 260px; top: 297px; display: flex; align-items: center; gap: 4px; }
  .social-row .rule { flex: 1; height: 1px; background: linear-gradient(90deg, transparent, var(--ink-orange)); }
  .social-row .rule.right { background: linear-gradient(90deg, var(--ink-orange), transparent); }
  .social-row .rule.left { margin-right: 2px; }
  .social-row .rule.right { margin-left: 2px; }
  .social-row .dot { width: 23px; height: 23px; border-radius: 50%; background: var(--ink-orange); flex: none; }
</style>
</head>
<body>
  <section class="card card-front">
    <div class="pattern-top" role="img" aria-label="Geometric triangle pattern in yellow and orange"></div>
    <div class="info-band"></div>
    <div class="pattern-bottom" role="img" aria-label="Geometric triangle pattern in orange and yellow"></div>

    <div class="identity">
      <div class="name">CORINNE V.</div>
      <div class="role">Communication Coach</div>
      <div class="role">Lead Storyteller</div>
    </div>
    <div class="divider"></div>
    <ul class="contacts">
      <li><svg viewBox="0 0 24 24"><path d="M6.6 10.8a15.1 15.1 0 0 0 6.6 6.6l2.2-2.2a1 1 0 0 1 1-.25 11.4 11.4 0 0 0 3.6.57 1 1 0 0 1 1 1V20a1 1 0 0 1-1 1A17 17 0 0 1 3 4a1 1 0 0 1 1-1h3.5a1 1 0 0 1 1 1c0 1.25.2 2.45.57 3.57a1 1 0 0 1-.25 1z"/></svg>514-555-0147</li>
      <li><svg viewBox="0 0 24 24"><path d="M7 1h10a2 2 0 0 1 2 2v18a2 2 0 0 1-2 2H7a2 2 0 0 1-2-2V3a2 2 0 0 1 2-2zm0 3v14h10V4zm5 15.5a1 1 0 1 0 0 2 1 1 0 0 0 0-2z"/></svg>514-555-0183.</li>
      <li><svg viewBox="0 0 24 24"><path d="M2 5h20v14H2zm2 2v.5l8 5 8-5V7zm0 2.8V17h16V9.8l-8 5z"/></svg>corinne@fernquill.com</li>
      <li><svg viewBox="0 0 24 24"><path d="M12 2a10 10 0 1 0 0 20 10 10 0 0 0 0-20zm-1 17.9A8 8 0 0 1 4.2 10.6L9 15.4v1a2 2 0 0 0 2 2zm6.9-2.5A2 2 0 0 0 16 16h-1v-3a1 1 0 0 0-1-1H8v-2h2a1 1 0 0 0 1-1V7h2a2 2 0 0 0 2-2v-.4a8 8 0 0 1 2.9 12.8z"/></svg>www.fernquill.com</li>
    </ul>
  </section>

  <section class="card card-back">
    <div class="brand-mark"></div>
    <div class="brand-name">FERNQUILL</div>
    <div class="motto">1 STORY &nbsp;1 VOICE</div>
    <div class="tagline">Telling Stories as bold as you</div>
    <div class="social-row">
      <span class="rule left"></span>
      <span class="dot"></span>
      <span class="dot"></span>
      <span class="dot"></span>
      <span class="rule right"></span>
    </div>
  </section>
</body>
</html>
```